Fatigued and Overloaded by COVID Messages? We need original illustrations to show that.

Everywhere you look there are messages about COVID. That is leading many people to feel fatigued and overloaded by the messages.

We surveyed U.S. adults March 20th - 24th, 2020 and measured message fatigue, information overload, perceived repetition, and perceived exaggeration. Here is how participants responded:

When it comes to coronavirus . . .
55% feel exhausted by all the messages.
54% feel overloaded by the amount of information.
51% feel that the messages are repetitive.
47% feel like messages exaggerate how bad it is.

In other words, almost half of U.S. adults show signs of message fatigue, information overload, perceived message repetition, and perceived message exaggeration.

We will continue to survey 400 adults every week for the next 16 weeks. Each time we will measure message fatigue, information overload, perceived repetition, and perceived exaggeration. We expect that it will increase over time.

What are we looking for? We need innovative and original illustrations that attempt to communicate these findings. The illustrations would visualize message fatigue, information overload, perceived message repetition, and perceived message exaggeration.

What sort of visual are we looking for? Our preference is for an original illustration (or set of illustrations). Our preference is for creative and powerful illustrations, but we are also open to the creative and well-executed infographics.

We need these images fast . We will award monetary prizes to the 3 best designs. If we like more than that, then we might purchase more (e.g., in past contests, we have purchased as many as 30 designs).

What we will need:
(1) The illustrations must be original and we will need the photoshop and/or illustrator files for all artwork. (By original, we mean that the illustrations are 100% created by you. Our organization requires that we utilize only original illustrated work. We have had issues with free imagery being pirated and reposted as free. We sidestep that issue by just having everything created.)

(2) The illustration should say, somewhere: "Based on a survey of 400 U.S. adults conducted March 20 - 24th, 2020."

(3) We will have almost 4 months worth of data by the time this is done. In other words, the illustrations might be able to help us present that weekly data.

(4) We have conducted other Artvendo projects. It might be helpful to examine designs we liked in the past. For example, here is another COVID project we just finished:

https://jobs.artvendo-example.com/job/5162048

Target Market(s)

U.S. adults

Requirements
Must have
• Original illustrations. Mobile friendly design. People will view this on their smartphones.
Nice to have
• A design that we can use to communicate the data across time.

```html
<!DOCTYPE html>
<html lang="en">
<head>
<meta charset="utf-8">
<title>Message Fatigue Survey</title>
<link href="https://fonts.googleapis.com/css2?family=Montserrat:wght@400;600;800;900&display=swap" rel="stylesheet">
<style>
  :root{
    --green-top:#2af07a;
    --green-mid:#17d08f;
    --teal:#14b2b0;
    --blue:#1c82e8;
    --white:#ffffff;
    --ink:#050505;
    --pie-red:#ed1c24;
    --panel:rgba(255,255,255,0.13);
    --virus:rgba(40,150,60,0.35);
  }
  *{margin:0;padding:0;box-sizing:border-box}
  html,body{width:1062px;height:1200px;overflow:hidden;background:#fff}
  .poster{
    position:relative;width:1062px;height:1200px;overflow:hidden;
    background:linear-gradient(160deg,var(--green-top) 0%,var(--green-mid) 35%,var(--teal) 70%,var(--blue) 100%);
    font-family:'Montserrat',sans-serif;
  }
  .header-band{
    position:absolute;left:0;top:0;width:1062px;height:210px;
    background:rgba(255,255,255,0.07);border-radius:0 0 42px 42px;
  }
  .headline{
    position:absolute;left:0;top:38px;width:1062px;text-align:center;
    color:var(--white);font-weight:900;font-size:35.5px;line-height:44px;white-space:nowrap;
  }
  .subhead{
    position:absolute;left:0;top:230px;width:1062px;text-align:center;
    color:var(--ink);font-weight:900;font-size:32.5px;
  }
  .results-panel{
    position:absolute;left:16px;top:293px;width:1015px;height:615px;
    background:var(--panel);border-radius:44px;
  }
  .virus-mark{position:absolute;border-radius:50%;background:var(--virus)}
  .stat{position:absolute}
  .stat svg{position:absolute;overflow:visible}
  .stat-value{
    position:absolute;color:var(--white);font-weight:900;font-size:32px;white-space:nowrap;
    transform:translate(-50%,-50%);
  }
  .stat-value .pct{font-weight:400;font-size:28px}
  .stat-caption{
    position:absolute;width:360px;margin-left:-180px;text-align:center;
    color:var(--white);font-weight:800;font-size:22px;line-height:26px;
  }
  .art{position:absolute;border-radius:18px}
  .art-messages{background:linear-gradient(135deg,#4a86c4,#dcb58c)}
  .art-overload{background:linear-gradient(180deg,#e8522e,#f2842a)}
  .art-repetition{background:linear-gradient(180deg,#3f9a64,#1f7a48)}
  .art-exaggeration{background:linear-gradient(180deg,#d04048,#b8303a)}
  .summary-panel{
    position:absolute;left:16px;top:972px;width:1015px;height:260px;
    background:var(--panel);border-radius:44px 44px 0 0;
  }
  .summary{
    position:absolute;left:0;top:1010px;width:1062px;text-align:center;
    color:var(--ink);font-weight:900;font-size:29.5px;line-height:35px;white-space:nowrap;
  }
  .source{
    position:absolute;left:0;top:1166px;width:1062px;text-align:center;
    color:var(--white);font-weight:400;font-size:23px;white-space:nowrap;
  }
</style>
</head>
<body>
<main class="poster">
  <div class="header-band"></div>
  <div class="virus-mark" role="img" aria-label="Faint virus particle decoration" style="left:58px;top:182px;width:92px;height:92px"></div>
  <div class="virus-mark" role="img" aria-label="Faint virus particle decoration" style="left:578px;top:325px;width:58px;height:58px"></div>
  <div class="virus-mark" role="img" aria-label="Faint virus particle decoration" style="left:226px;top:858px;width:62px;height:62px"></div>
  <div class="virus-mark" role="img" aria-label="Faint virus particle decoration" style="left:846px;top:850px;width:122px;height:122px"></div>
  <div class="virus-mark" role="img" aria-label="Faint virus particle decoration" style="left:42px;top:1090px;width:82px;height:82px"></div>

  <h1 class="headline">We surveyed U.S. adults March 20th - 24th, 2020 and<br>measured message fatigue, information overload,<br>perceived repetition, and perceived exaggeration</h1>
  <h2 class="subhead">Here is how participants responded</h2>

  <section class="results-panel"></section>

  <div class="stat">
    <svg style="left:115px;top:375px" width="104" height="104" viewBox="-52 -52 104 104">
      <path d="M0 0 L0 -52 A52 52 0 1 0 16.07 49.46 Z" fill="var(--pie-red)"/>
    </svg>
    <div class="stat-value" style="left:182px;top:430px">55<span class="pct">%</span></div>
    <p class="stat-caption" style="left:164px;top:490px">feel exhausted<br>by all the messages</p>
  </div>
  <div class="art art-messages" role="img" aria-label="Illustration of a tired woman surrounded by messages, envelopes and news" style="left:287px;top:372px;width:168px;height:164px"></div>

  <div class="stat">
    <svg style="left:704px;top:369px" width="104" height="104" viewBox="-52 -52 104 104">
      <path d="M0 0 L0 -52 A52 52 0 1 0 6.52 51.59 Z" fill="var(--pie-red)"/>
    </svg>
    <div class="stat-value" style="left:770px;top:424px">54<span class="pct">%</span></div>
    <p class="stat-caption" style="left:749px;top:493px">feel overloaded by the<br>amount of information</p>
  </div>
  <div class="art art-overload" role="img" aria-label="Illustration of an overwhelmed man with an explosion above his head" style="left:905px;top:365px;width:106px;height:177px"></div>

  <div class="stat">
    <svg style="left:146px;top:651px" width="104" height="104" viewBox="-52 -52 104 104">
      <path d="M0 0 L0 -52 A52 52 0 0 0 -3.27 51.90 Z" fill="var(--pie-red)"/>
    </svg>
    <div class="stat-value" style="left:214px;top:706px">51<span class="pct">%</span></div>
    <p class="stat-caption" style="left:188px;top:782px">feel that the messages<br>are repetitive</p>
  </div>
  <div class="art art-repetition" role="img" aria-label="Illustration of repeated chat messages" style="left:336px;top:653px;width:89px;height:177px"></div>

  <div class="stat">
    <svg style="left:703px;top:646px" width="104" height="104" viewBox="-52 -52 104 104">
      <path d="M0 0 L0 -52 A52 52 0 0 0 -9.74 51.08 Z" fill="var(--pie-red)"/>
    </svg>
    <div class="stat-value" style="left:770px;top:701px">47<span class="pct">%</span></div>
    <p class="stat-caption" style="left:763px;top:782px">feel like messages<br>exaggerate how bad it is</p>
  </div>
  <div class="art art-exaggeration" role="img" aria-label="Illustration contrasting true and false messages" style="left:922px;top:643px;width:93px;height:186px"></div>

  <section class="summary-panel"></section>
  <p class="summary">In other words, almost half of U.S. adults show signs of<br>message fatigue, information overload, perceived message<br>repetition, and perceived message exaggeration</p>
  <p class="source">"Based on a survey of 400 U.S. adults conducted March 20 - 24th, 2020."</p>
</main>
</body>
</html>
```